13 Tavo - new website design project

Our company Tavo Electrical is developing a new lead generation website focused on Electrical, LED Lighting and Solar Power. We need a high converting website.

Example of our current website is www.tavoelectrical.com.au You can take content from this website for this new design. Our colours are red, black and white. For our new website we would like to promote Tavo, Bright Days Ahead. Please listen to the jingle.

The below link is the company jingle that we have developed.
http://www.tunecraftaudio.com.au/tav-tc-v1/

The key for this brief is to generate leads for Electrical, LED Lighting (for commercial) and Solar Power & Storage.

Target Market(s)

Business owners in Melbourne Victoria

Number of Pages Required

4 page

Colors
ec1f27
ffffff

Requirements
Must have
• This page must be clean, be in line with company branding and a high converting lead website.

```html
<!DOCTYPE html>
<html lang="en">
<head>
<meta charset="utf-8">
<title>Tavo Electrical</title>
<link rel="stylesheet" href="https://fonts.googleapis.com/css2?family=Roboto:wght@300;400;500;700&display=swap">
<style>
:root{
  --red:#d71f27;
  --red-bright:#ec1f27;
  --ink:#22252c;
  --black:#0b0b0c;
  --bar:#1c1f26;
  --grey:#f1f0f1;
  --grey-2:#e8e8ea;
  --text:#555;
  --white:#fff;
}
*{margin:0;padding:0;box-sizing:border-box}
html,body{width:1200px;height:2304px;overflow:hidden}
body{position:relative;font-family:'Roboto',sans-serif;color:var(--ink);background:var(--white)}
.abs{position:absolute}

/* top bar + nav */
.top-bar{left:0;top:0;width:1200px;height:23px;background:var(--bar)}
.top-phone{right:250px;top:2px;display:flex;align-items:center;gap:4px;color:var(--white);font-weight:700;font-size:15px}
.tag{background:var(--red);color:var(--white);font-size:10px;font-weight:700;padding:1px 4px}
.nav{left:0;top:23px;width:1200px;height:35px;background:var(--white)}
.logo-box{left:248px;top:0;width:107px;height:58px;background:#e9e9ea;display:flex;flex-direction:column;align-items:center;justify-content:center}
.logo-box .name{font-weight:700;font-size:22px;color:var(--ink);line-height:1}
.logo-box .sub{font-size:6px;color:var(--red);margin-top:3px}
.menu{right:251px;top:12px;display:flex;gap:14px;font-size:10px;font-weight:500;color:#111}

/* hero */
.hero{left:0;top:58px;width:1200px;height:369px;background:linear-gradient(100deg,#efefef 0%,#fafafa 40%,#e9e9e9 60%);overflow:hidden}
.hero-art{left:0;top:0}
.hero-photo{left:300px;top:35px;width:148px;height:158px;background:linear-gradient(160deg,#e6e7ea 0%,#c9ccd3 45%,#3a3f4d 100%)}
.hero-card{left:248px;top:193px;width:278px;height:166px;background:var(--ink);padding:18px 20px}
.hero-card h1{color:var(--red-bright);font-size:22px;font-weight:500;letter-spacing:.3px}
.hero-card .lead{color:var(--white);font-size:14px;font-weight:300;margin-top:6px}
.hero-card .points{color:var(--white);font-size:14px;font-weight:500;line-height:23px;margin-top:10px}
.hero-rule{left:0;top:427px;width:1200px;height:2px;background:var(--red)}

/* welcome */
.welcome{left:0;top:429px;width:1200px;height:160px;background:var(--grey);text-align:center}
.welcome h2{margin-top:22px;font-size:24px;font-weight:400;letter-spacing:.5px}
.divider{width:490px;height:12px;margin:6px auto 0;position:relative}
.divider::before{content:"";position:absolute;left:0;right:0;top:6px;height:1px;background:#777}
.divider::after{content:"";position:absolute;left:240px;top:2px;width:7px;height:7px;border:2px solid var(--red);background:var(--grey);transform:rotate(45deg)}
.welcome p{width:700px;margin:12px auto 0;font-size:10px;line-height:17px;color:var(--text);font-weight:300}
.pointer{left:591px;top:589px;width:0;height:0;border-left:9px solid transparent;border-right:9px solid transparent;border-top:8px solid var(--red)}

/* services */
.services{left:248px;top:622px;width:702px;display:flex;gap:13px}
.service{width:225px;height:335px;background:var(--grey);text-align:center;position:relative}
.service .photo{height:145px}
.ph-solar{background:linear-gradient(160deg,#f3d0b4,#9fb6d3 55%,#2c4f8a)}
.ph-led{background:linear-gradient(160deg,#1a4ea3,#4a86d6 55%,#0e2f6a)}
.ph-elec{background:linear-gradient(160deg,#c8c8c8,#d14a3c 55%,#6b6b6b)}
.service .icon{position:absolute;left:94px;top:127px;width:36px;height:36px;border-radius:50%;background:var(--ink);display:flex;align-items:center;justify-content:center}
.service h3{margin-top:30px;font-size:15px;font-weight:500}
.service p{margin:8px 10px 0;font-size:10px;line-height:16px;color:var(--text);font-weight:300;height:64px;overflow:hidden}
.btn-dark{display:inline-block;margin-top:16px;width:148px;height:33px;line-height:33px;background:var(--ink);color:var(--white);font-size:14px}

/* why */
.why{left:0;top:994px;width:1200px;height:538px;background:var(--grey-2)}
.why h2{text-align:center;margin-top:34px;font-size:24px;font-weight:400;letter-spacing:.5px}
.steps-line{left:300px;top:120px;width:3px;height:352px;background:var(--red)}
.step{left:270px;width:660px;display:flex;gap:18px}
.step .num{flex:none;width:64px;height:64px;border-radius:50%;border:3px solid var(--red);background:var(--white);display:flex;align-items:center;justify-content:center;font-size:20px;font-weight:500}
.step h4{color:var(--red);font-size:15px;font-weight:500;margin-top:6px}
.step p{font-size:9.5px;line-height:17px;color:var(--text);margin-top:6px}

/* clients */
.clients-title{left:0;top:1572px;width:1200px;text-align:center;font-size:24px;font-weight:400;letter-spacing:.5px}
.clients-left{left:0;top:1626px;width:595px;height:326px;background:var(--grey-2)}
.clients-right{left:595px;top:1626px;width:605px;height:326px;background:var(--ink)}
.client{width:144px;height:84px;background:var(--white);border:4px solid #dadada;display:flex;align-items:center;justify-content:center;font-size:16px;font-weight:700;color:var(--ink);text-align:center}
.quote-avatar{left:632px;top:1705px}
.quote-name{left:698px;top:1716px;color:var(--white);font-size:11px;line-height:13px}
.quote-name b{font-weight:500;display:block}
.quote-text{left:644px;top:1780px;width:310px;color:var(--white);font-size:12px;font-style:italic;line-height:19px;font-weight:300}
.dots{left:650px;top:1868px;display:flex;gap:7px}
.dots span{width:7px;height:7px;border-radius:50%;background:var(--white)}
.dots .on{background:var(--red)}

/* footer */
.footer{left:0;top:1998px;width:1200px;height:279px;background:var(--black)}
.f-logo{left:375px;top:64px;color:var(--white);font-size:26px;font-weight:700;display:flex;align-items:center;gap:6px}
.f-logo i{width:12px;height:12px;background:var(--red);display:block}
.f-about{left:373px;top:108px;width:200px;color:#cfcfcf;font-size:7.8px;line-height:12.5px}
.btn-red{left:373px;top:198px;width:90px;height:18px;background:var(--red);color:var(--white);font-size:9px;text-align:center;line-height:18px}
.f-divider{left:600px;top:30px;width:1px;height:220px;background:#333}
.f-phone{left:630px;top:48px}
.f-number{left:630px;top:70px;display:flex;align-items:center;gap:5px;color:var(--white);font-size:22px;font-weight:700}
.f-number .tag{font-size:13px;padding:2px 5px}
.social{left:630px;top:124px;display:flex;gap:8px}
.social span{width:28px;height:28px;border-radius:50%;background:#5b5f68}
.quick{left:638px;top:182px;color:var(--red);font-size:11px}
.quick-links{left:638px;top:201px;display:flex;gap:8px;color:var(--white);font-size:8.5px}
.bottom-bar{left:0;top:2277px;width:1200px;height:27px;background:var(--bar);color:#ccc;font-size:8.5px;text-align:center;line-height:27px}
</style>
</head>
<body>

<div class="abs top-bar"></div>
<div class="abs top-phone">
  <svg width="13" height="11" viewBox="0 0 13 11"><path d="M1 4c0-2 3-3 5.5-3S12 2 12 4l-2 1-1-2H4L3 5z M3 6h7l1 4H2z" fill="#ec1f27"/></svg>
  137284 <span class="tag">TAVO</span>
</div>

<header class="abs nav">
  <nav class="abs menu">
    <span>Home</span><span>Tavo Story</span><span>Our Work</span><span>Contact Us</span><span>Electrical</span><span>Led Lighting</span><span>Solar Power</span>
  </nav>
</header>
<div class="abs logo-box"><span class="name">TAVO</span><span class="sub">Bright Days Ahead</span></div>

<section class="abs hero">
  <svg class="abs hero-art" width="1200" height="369" viewBox="0 0 1200 369" role="img" aria-label="Collage of an LED bulb, an electrician testing wiring and a technician installing solar panels">
    <defs>
      <linearGradient id="gBulb" x1="0" y1="0" x2="1" y2="1"><stop offset="0" stop-color="#5e9ae0"/><stop offset="1" stop-color="#123c86"/></linearGradient>
      <linearGradient id="gWire" x1="0" y1="0" x2="1" y2="1"><stop offset="0" stop-color="#6a6a6a"/><stop offset=".5" stop-color="#d6bba7"/><stop offset="1" stop-color="#7a1d1d"/></linearGradient>
      <linearGradient id="gSolar" x1="0" y1="0" x2="1" y2="1"><stop offset="0" stop-color="#2f5f9e"/><stop offset=".6" stop-color="#3b6fb6"/><stop offset="1" stop-color="#1b3a6b"/></linearGradient>
    </defs>
    <path d="M610 369 C700 200 760 80 790 0 L1200 0 L1200 369 Z" fill="url(#gBulb)"/>
    <path d="M785 369 C840 230 900 90 930 0 L1200 0 L1200 369 Z" fill="#fff"/>
    <path d="M797 369 C850 230 910 90 940 0 L1200 0 L1200 369 Z" fill="url(#gWire)"/>
    <path d="M1000 369 C1030 230 1075 90 1095 0 L1200 0 L1200 369 Z" fill="#fff"/>
    <path d="M1012 369 C1040 230 1085 90 1105 0 L1200 0 L1200 369 Z" fill="url(#gSolar)"/>
  </svg>
  <div class="abs hero-photo" role="img" aria-label="Photo of a smiling electrician in work gear"></div>
  <div class="abs hero-card">
    <h1>WELCOME TO 13TAVO</h1>
    <p class="lead">Australia,s largeest flly integrated</p>
    <p class="points">Electrical &amp;energy<br>Solutions Provider<br>Led Lighting</p>
  </div>
</section>
<div class="abs hero-rule"></div>

<section class="abs welcome">
  <h2>WELCOME &nbsp;TO TAVO</h2>
  <div class="divider"></div>
  <p>Lorem Ipsum is simply dummy text of the printing and typesetting industry. Lorem Ipsum has been the industry's standard dummy text ever since the 1500s, when an unknown printer took a galley of type and scrambled it to make a type specimen book. It has survived not only five centuries, but also the leap into electronic typesetting.</p>
</section>
<div class="abs pointer"></div>

<section class="abs services">
  <article class="service">
    <div class="photo ph-solar" role="img" aria-label="Technicians installing solar panels on a roof"></div>
    <div class="icon"><svg width="16" height="16" viewBox="0 0 16 16"><circle cx="5" cy="5" r="2.5" fill="#fff"/><path d="M7 9h8l-2 6H5z" fill="none" stroke="#fff" stroke-width="1.3"/></svg></div>
    <h3>Solar Power</h3>
    <p>Lorem Ipsum is simply dummy text of the printing and typesetting industry. Lorem Ipsum has been the industry's standard dummy text ever since the 1500s, when an unknown printer took a galley of type and scrambled it</p>
    <span class="btn-dark">Read More</span>
  </article>
  <article class="service">
    <div class="photo ph-led" role="img" aria-label="Glowing LED light bulbs"></div>
    <div class="icon"><svg width="14" height="16" viewBox="0 0 14 16"><circle cx="7" cy="6" r="5" fill="#fff"/><rect x="4.5" y="11" width="5" height="4" fill="#fff"/></svg></div>
    <h3>Led Lighting</h3>
    <p>Lorem Ipsum is simply dummy text of the printing and typesetting industry. Lorem Ipsum has been the industry's standard dummy text ever since the 1500s, when an unknown printer took a galley of type and scrambled it</p>
    <span class="btn-dark">Read More</span>
  </article>
  <article class="service">
    <div class="photo ph-elec" role="img" aria-label="Multimeter testing a switchboard"></div>
    <div class="icon"><svg width="16" height="16" viewBox="0 0 16 16"><path d="M3 13l4-4M6 5l5 5 3-3-5-5zM9 2l2-2M14 7l2-2" stroke="#fff" stroke-width="1.6" fill="#fff"/></svg></div>
    <h3>Electrical</h3>
    <p>Lorem Ipsum is simply dummy text of the printing and typesetting industry. Lorem Ipsum has been the industry's standard dummy text ever since the 1500s, when an unknown printer took a galley of type and scrambled it</p>
    <span class="btn-dark">Read More</span>
  </article>
</section>

<section class="abs why">
  <h2>WHY CHOOSE US?</h2>
  <div class="abs steps-line"></div>
  <div class="abs step" style="top:90px"><div class="num">1</div><div><h4>Professional service</h4><p>When you hire a Tavo Electrical Electrician you will get a professional and well-presented Electrician that comes skilled and ready to do the job</p></div></div>
  <div class="abs step" style="top:178px"><div class="num">2</div><div><h4>5 year workmanship guarantee</h4><p>You can buy with confidence as all of our work has a 5 year workmanship guarantee. For your peace of mind, we unconditionally back our electrical work. We will come back to fix any problems at our own expense.</p></div></div>
  <div class="abs step" style="top:266px"><div class="num">3</div><div><h4>Value for Money</h4><p>We provide extremely competitive pricing, which means you get value for money on quality that is comparable to the best in the industry.</p></div></div>
  <div class="abs step" style="top:354px"><div class="num">4</div><div><h4>Environmentally friendly</h4><p>We a committed to reducing carbon emissions by installing Solar Power and upgrading sites to LED Lighting. In addition to reducing the carbon emissions we recycle Fluorescent Tubes, Highbay Globes, Metal and Cardboard.</p></div></div>
  <div class="abs step" style="top:440px"><div class="num">5</div><div><h4>Fully insured</h4><p>Tavo Electrical is fully insured and equipped to handle break downs and service call outs.</p></div></div>
</section>

<h2 class="abs clients-title">OUR SATISFIED CLIENTS INCLUDE...</h2>
<section class="abs clients-left"></section>
<div class="abs client" style="left:248px;top:1694px">Maple Grill</div>
<div class="abs client" style="left:407px;top:1694px">Heron Pipeworks</div>
<div class="abs client" style="left:248px;top:1793px">Outback Surplus</div>
<div class="abs client" style="left:407px;top:1793px">Lumera</div>

<section class="abs clients-right"></section>
<svg class="abs quote-avatar" width="59" height="59" viewBox="0 0 59 59"><circle cx="29.5" cy="29.5" r="28" fill="#fff"/><circle cx="29.5" cy="29.5" r="17" fill="none" stroke="#9a9ea6" stroke-width="5"/></svg>
<div class="abs quote-name"><b>Dana Kell</b>Berwick South VIC</div>
<p class="abs quote-text">Excellent work and very professional. Marcus takes time to explain everything and demonstrate workings. Very clear precise and accurate."</p>
<div class="abs dots"><span></span><span class="on"></span><span></span></div>

<footer class="abs footer">
  <div class="abs f-logo"><i></i>TAVO</div>
  <p class="abs f-about">Tavo Electrical was formed to be an expert Electricity Contracting Company providing services to all Residential and Commercial Customers. With over 10 years of experience, Tavo Electrical has developed a highly-experienced team of professionals that ensure all our customer expectations are met.</p>
  <div class="abs btn-red">Read More</div>
  <div class="abs f-divider"></div>
  <svg class="abs f-phone" width="22" height="18" viewBox="0 0 13 11"><path d="M1 4c0-2 3-3 5.5-3S12 2 12 4l-2 1-1-2H4L3 5z M3 6h7l1 4H2z" fill="#ec1f27"/></svg>
  <div class="abs f-number">137284 <span class="tag">TAVO</span></div>
  <div class="abs social"><span></span><span></span><span></span><span></span></div>
  <div class="abs quick">Quick Link</div>
  <div class="abs quick-links"><span>Led Lighting</span><span>Solar Power</span><span>Electrical</span><span>Career</span></div>
</footer>
<div class="abs bottom-bar">A © 2016 All rights reserved | Privacy Policy. Design &amp; Development by brightgridstudio.com.au</div>

</body>
</html>
```